Verpackungen für Matcha Tee Sticks
Zielgruppe
Premium Matcha Tee Sticks in hochwertiger Qualität. Die Umverpackung wird voraussichtlich in Dosen sein.
Unsere Zielgruppe sind Menschen mit Lust auf guten Geschmack und eine Prise Luxus, ReisSportler, Gesundheitsbewusste und Genießer.
Aufgabenstellung
Wir brauchen ein Logo & eine Verpackung (Banderole) für Dosen (Durchmesser: 63/ Höhe: 105 mm) für unser Label 'teefix4go'.
Modern, Luxuriös, Schlicht - Farben: gold, grün, schwarz, weiß (sind aber auch für andere Farbvarianten offen)
Die Matcha Sticks werden wahrscheinlich in schwarzen oder weißen oder goldenen Dosen verkauft werden.
Abmessungen Banderole: ca. Höhe: 105 / Breite:178mm
@all: Tendenziell sollen die Vorschläge noch luxuriöser und feiner werden. z.B. schwarzer Hintergrund mit feiner Schrift oder z.B. die Marke QRP Brew aus Singapur hat erlesene Tees in luxuriösem Design. Inspirierende Marken: Belnoix Vamont (Kekse, Kerzen), Ulla Verbeck (Kosmetik), Tissand Oulmes (Tee), Brevo oder ZAR Tee....
Es darf gerne ein Eyecatcher sein, IT-piece, must-have.... Eine Dose, die man lieber sammelt als nach Gebrauch wegzuschmeißen. Ihr könnt Euch auch vom Farbschema lösen. Das war nur ein erster Gedanke, da Matcha grün ist und die Dose voraussichtlich schwarz und gold Luxus verkörpert. Stellt Euch die Einkaufsmall in Dubai vor. Da heißt es auffallen. Knallorange....es muss rocken.
Wir sind gespannt auf weitere Vorschläge und möchten uns auch für die eingegangen Vorschläge bedanken. Wir wissen, dass da schon einiges an Arbeit drinsteckt.
Happy Weekend :)

```html
<!DOCTYPE html>
<html lang="de">
<head>
<meta charset="utf-8">
<title>teefix4go – Banderole Premium Matcha Tee Sticks</title>
<link rel="stylesheet" href="https://fonts.googleapis.com/css2?family=Cabin:wght@400;500;600&display=swap">
<style>
  :root {
    --page-bg: #ffffff;
    --label-green: #55642a;
    --label-green-light: #6e7e39;
    --label-green-pale: #7d8d46;
    --label-green-deep: #46531f;
    --panel-green: #2f3a19;
    --band-green: #29331a;
    --gold: #d8b24c;
    --gold-soft: #b89a4a;
    --cream: #e9e2c8;
  }
  * { margin: 0; padding: 0; box-sizing: border-box; }
  html, body {
    width: 1200px;
    height: 960px;
    overflow: hidden;
    background: var(--page-bg);
  }
  .canvas {
    position: relative;
    width: 1200px;
    height: 960px;
    background: var(--page-bg);
  }
  .banderole {
    position: absolute;
    left: 50px;
    top: 155px;
    width: 1100px;
    height: 649px;
    overflow: hidden;
    background: var(--label-green);
  }
  .banderole__pattern {
    position: absolute;
    inset: 0;
    background:
      radial-gradient(ellipse 38% 30% at 22% 62%, rgba(125, 141, 70, 0.55) 0%, rgba(125, 141, 70, 0) 100%),
      radial-gradient(ellipse 38% 30% at 78% 62%, rgba(125, 141, 70, 0.55) 0%, rgba(125, 141, 70, 0) 100%),
      radial-gradient(ellipse 30% 26% at 50% 52%, rgba(125, 141, 70, 0.5) 0%, rgba(125, 141, 70, 0) 100%),
      radial-gradient(ellipse 32% 22% at 18% 22%, rgba(110, 126, 57, 0.6) 0%, rgba(110, 126, 57, 0) 100%),
      radial-gradient(ellipse 32% 22% at 82% 22%, rgba(110, 126, 57, 0.6) 0%, rgba(110, 126, 57, 0) 100%),
      radial-gradient(ellipse 45% 18% at 50% 96%, rgba(110, 126, 57, 0.55) 0%, rgba(110, 126, 57, 0) 100%),
      linear-gradient(90deg, var(--label-green-deep) 0%, var(--label-green) 18%, var(--label-green-light) 50%, var(--label-green) 82%, var(--label-green-deep) 100%);
  }
  .banderole__rule {
    position: absolute;
    left: 0;
    right: 0;
    height: 1px;
    background: var(--gold-soft);
    opacity: 0.45;
  }
  .banderole__rule--top { top: 10px; }
  .banderole__rule--bottom { bottom: 10px; }
  .brand-panel {
    position: absolute;
    left: 405px;
    top: 0;
    width: 290px;
    height: 265px;
    background: linear-gradient(180deg, #34401c 0%, var(--panel-green) 100%);
    box-shadow: 0 4px 12px rgba(0, 0, 0, 0.3);
  }
  .brand-panel__frame {
    position: absolute;
    left: 12px;
    right: 12px;
    top: 0;
    bottom: 12px;
    border: 1px solid var(--gold-soft);
    border-top: none;
    opacity: 0.7;
  }
  .brand-panel__name {
    position: absolute;
    left: 0;
    right: 0;
    top: 104px;
    text-align: center;
    font-family: "Cabin", sans-serif;
    font-weight: 500;
    font-size: 50px;
    letter-spacing: 0.5px;
    color: var(--gold);
    line-height: 1;
  }
  .product-band {
    position: absolute;
    left: 0;
    right: 0;
    top: 464px;
    height: 90px;
    background: linear-gradient(180deg, #2f3a1b 0%, var(--band-green) 100%);
    box-shadow: 0 3px 8px rgba(0, 0, 0, 0.3);
    display: flex;
    flex-direction: column;
    align-items: center;
    justify-content: center;
    gap: 9px;
  }
  .product-band__title {
    font-family: "Cabin", sans-serif;
    font-weight: 500;
    font-size: 18px;
    letter-spacing: 0.6px;
    color: var(--gold);
  }
  .product-band__content {
    font-family: "Cabin", sans-serif;
    font-weight: 400;
    font-size: 12px;
    letter-spacing: 0.8px;
    color: var(--cream);
  }
</style>
</head>
<body>
  <main class="canvas">
    <section class="banderole">
      <div class="banderole__pattern" role="img" aria-label="Allover pattern of stylised flowers in light olive green on the green label"></div>
      <div class="banderole__rule banderole__rule--top"></div>
      <div class="banderole__rule banderole__rule--bottom"></div>

      <div class="brand-panel">
        <div class="brand-panel__frame"></div>
        <div class="brand-panel__name">teefix4go</div>
      </div>

      <div class="product-band">
        <p class="product-band__title">PREMIUM MATCHA TEE STICKS</p>
        <p class="product-band__content">XX STICKS á XX g</p>
      </div>
    </section>
  </main>
</body>
</html>
```